Business Card Design

i am looking a business card for a car rental company long with Taxi service also a logo.
Updates

what is the latest with my project

Industry/Entity Type

Business

Contact Information for Business Card

name of the Company is Brenmoor Auto Hire and Cab Services
Address: Kestrel Hill Village, St. Aldric's Parish Antigua
Tele# 558-2047/6194852-613-9075
Email: tolvipark@quenmail.net

Font styles to use
Script

```html
<!DOCTYPE html>
<html lang="en">
<head>
<meta charset="utf-8">
<title>Brenmoor Auto Hire and Cab Services – Business Card</title>
<link rel="stylesheet" href="https://fonts.googleapis.com/css2?family=Cookie&family=Carlito&display=swap">
<style>
  :root {
    --card-brown: #3a1100;
    --cream: #fff6ea;
    --emblem-tone: #4e2511;
  }
  html, body {
    margin: 0;
    padding: 0;
    width: 1200px;
    height: 733px;
    overflow: hidden;
    background: var(--card-brown);
  }
  .business-card {
    position: relative;
    width: 1200px;
    height: 733px;
    background: var(--card-brown);
    color: var(--cream);
  }
  .car-emblem {
    position: absolute;
    left: 65px;
    top: 62px;
    width: 388px;
    height: 184px;
    border-radius: 90px 120px 40px 40px;
    background: radial-gradient(ellipse at 45% 55%, var(--emblem-tone) 0%, var(--card-brown) 75%);
  }
  .company-name {
    position: absolute;
    left: 0;
    top: 288px;
    width: 1200px;
    margin: 0;
    text-align: center;
    font-family: "Cookie", cursive;
    font-weight: 400;
    font-size: 60px;
    line-height: 84px;
    letter-spacing: 1px;
  }
  .divider {
    position: absolute;
    left: 144px;
    top: 495px;
    width: 913px;
    height: 2px;
    background: var(--cream);
  }
  .contact-details {
    position: absolute;
    left: 0;
    top: 534px;
    width: 1200px;
    margin: 0;
    text-align: center;
    font-family: "Carlito", "Calibri", sans-serif;
    font-style: normal;
    font-size: 30px;
    line-height: 46px;
  }
  .contact-details span { display: block; }
</style>
</head>
<body>
  <div class="business-card">
    <div class="car-emblem" role="img" aria-label="Line-art sports car logo in cream strokes"></div>

    <h1 class="company-name">Brenmoor<br>Auto Hire and Cab Services</h1>

    <div class="divider"></div>

    <address class="contact-details">
      <span class="address">Kestrel Hill Village, St. Aldric's Parish Antigua,</span>
      <span class="phone">Tele# 558-2047/6194852-613-9075</span>
      <span class="email">Email: tolvipark@quenmail.net</span>
    </address>
  </div>
</body>
</html>
```